Corvanel Aviation Needs a New Website

1. Details about the company
The website is for a company that conducts businesses in Singapore, Africa and Australia. The name of the Company is Corvanel.
The services include
• Aviation engineering services
• Aviation consulting
• Aviation equipment supplies
• Aviation construction projects
• Aviation business development
2. The designing
• The design can be custom design or premium template redesign
• The theme must be very classy and corporate
• Images to be used on the site must represent the services that the company conducts (5 images)
• The company logo is supplied to be used on the homepage and for the favicon
• The design to be installed on www.corvanel-example.com
3. The Pages
There will be 5 pages.
a. Home
• With latest news widget (showing the 3 latest news)
• Socialbook, Chirper links
b. About us
c. News
• Weekly news will be posted on this page and the latest news widget will be shown on the homepage
d. Services
• With Request-for-a-quote plugin
e. Contact Us
• Phone numbers
• Fax numbers
• Email addresses
• Google map address plugin for up to 3 locations

```html
<!DOCTYPE html>
<html lang="en">
<head>
<meta charset="utf-8">
<title>Corvanel Aviation</title>
<link href="https://fonts.googleapis.com/css2?family=Roboto:ital,wght@0,300;0,400;0,500;0,700;1,400&family=Oswald:wght@500&display=swap" rel="stylesheet">
<style>
:root{
  --blue:#2f6fc4;
  --blue-dark:#1f56a8;
  --navy:#1d3f77;
  --ink:#222;
  --text:#555;
  --light:#f4f4f4;
  --line:#e2e2e2;
  --footer:#1e1e1e;
  --footer-field:#191919;
  --footer-text:#9a9a9a;
  --white:#fff;
}
*{box-sizing:border-box;margin:0;padding:0}
html,body{width:1200px;height:2293px;overflow:hidden}
body{position:relative;font-family:'Roboto',sans-serif;color:var(--text);background:var(--white)}
.abs{position:absolute}
a{color:inherit;text-decoration:none}

/* header */
.site-header{left:0;top:0;width:1200px;height:118px;background:var(--white)}
.header-contact{top:32px;display:flex;align-items:center;gap:14px}
.icon-ring{width:40px;height:40px;border:1.5px solid #555;border-radius:50%;display:flex;align-items:center;justify-content:center}
.header-contact .label{font-size:16px;color:#333}
.header-contact .value{font-size:18px;color:var(--navy);margin-top:4px}
.header-contact.email .value{font-size:15px;color:#666}
.brand{left:0;width:1200px;top:33px;display:flex;justify-content:center;align-items:center;gap:12px}
.brand-dot{width:14px;height:14px;border-radius:50%;background:var(--blue-dark)}
.brand-name{font-size:42px;font-weight:700;color:var(--blue-dark);letter-spacing:.5px}

/* nav */
.main-nav{left:0;top:118px;width:1200px;height:61px;background:linear-gradient(#3a7ad0,#2a64b8)}
.main-nav ul{list-style:none;display:flex;height:61px;padding-left:99px}
.main-nav li{color:var(--white);font-size:15px;line-height:61px;padding:0 33px 0 0}
.main-nav li+li{border-left:1px solid rgba(255,255,255,.15);padding-left:34px}
.nav-social{right:99px;top:16px;display:flex;gap:6px}
.nav-social span{width:23px;height:23px;border:1.5px solid var(--white);border-radius:50%}

/* hero */
.hero{left:0;top:179px;width:1200px;height:512px;background:linear-gradient(160deg,#9eb3c9 0%,#5f7a97 35%,#c99a78 55%,#6d86a4 75%,#c8d2dc 100%)}
.hero-title{left:0;width:1200px;top:70px;text-align:center;font-family:'Oswald',sans-serif;font-weight:500;font-size:58px;color:var(--white)}
.hero-arrow{top:243px;width:36px;height:36px;border-radius:50%;background:rgba(60,60,60,.55);display:flex;align-items:center;justify-content:center}

/* services */
.section-title{left:0;width:1200px;top:716px;text-align:center;font-size:32px;color:var(--navy);font-weight:400}
.round-arrow{top:727px;width:28px;height:28px;border:1px solid #bbb;border-radius:50%;display:flex;align-items:center;justify-content:center}
.service{top:789px;width:234px}
.service .photo{height:171px}
.service h3{font-size:19px;font-weight:400;color:var(--ink);margin:17px 0 10px 3px;white-space:nowrap}
.service p{font-size:12.5px;line-height:20px;color:#555;margin-left:3px}
.read-more{display:block;font-size:14px;color:var(--blue-dark);margin:14px 0 0 3px}

/* welcome */
.welcome{left:0;top:1139px;width:1200px;height:381px;background:var(--light)}
.video{left:99px;top:44px;width:406px;height:288px;border:1px solid #ccc;background:var(--white)}
.video .frame{height:259px;background:linear-gradient(160deg,#8fb3d6,#4d7fae 60%,#3b6a92)}
.video .bar{height:27px;display:flex;align-items:center;padding:0 10px;gap:10px;font-size:8px;color:#333}
.video .track{width:200px;height:3px;background:#555;position:relative}
.video .track i{position:absolute;left:0;top:0;height:3px;width:95px;background:#d33}
.video .vol{width:36px;height:3px;background:#d33}
.welcome-body{left:555px;top:40px;width:511px}
.welcome-body h2{font-size:33px;font-weight:500;color:var(--ink);letter-spacing:.3px}
.welcome-body h2 span{color:var(--blue-dark)}
.welcome-body p{font-size:12.5px;line-height:20.5px;color:#333;margin-top:12px}
.ticks{list-style:none;margin-top:17px}
.ticks li{font-size:11.5px;color:#333;height:34px;display:flex;align-items:center;gap:14px;border-bottom:1px solid var(--line)}
.ticks li:last-child{border-bottom:0}
.tick{width:10px;height:10px;border:2px solid var(--blue-dark);border-radius:50%;position:relative}
.tick::after{content:"";position:absolute;left:1.5px;top:1.5px;width:3px;height:3px;background:var(--blue-dark);border-radius:50%}
.btn{display:inline-block;background:#2a4fae;color:var(--white);font-size:15px;width:133px;height:37px;line-height:37px;text-align:center;border-radius:2px;margin-top:14px}

/* news */
.col-title{font-size:20px;color:var(--ink);font-weight:400}
.news-item{left:98px;width:672px;height:148px}
.news-item .photo{position:absolute;left:0;top:0;width:231px;height:148px}
.news-item .body{position:absolute;left:257px;top:0;width:415px}
.news-item h4{font-size:17px;font-weight:400;color:#222}
.news-item .date{font-size:13px;color:var(--blue-dark);margin-top:15px}
.news-item p{font-size:11.5px;line-height:20.5px;color:#444;margin-top:10px}
.news-item .more{font-size:12px;color:var(--blue-dark);margin-top:10px;display:flex;align-items:center;gap:8px}

.testimonial{left:806px;top:1607px;width:296px;height:338px;background:var(--light);border:1px solid #e6e6e6;padding:20px 22px}
.testimonial h5{font-size:12.5px;font-weight:400;color:#333;line-height:21px}
.testimonial .quote{font-size:12.5px;line-height:21px;color:#333;margin-top:16px;position:relative;padding:0 6px}
.testimonial .quote::before{content:"\201C";position:absolute;left:-8px;top:-6px;font-size:22px;color:#aaa}
.testimonial .quote::after{content:"\201D";position:absolute;right:-8px;bottom:-26px;font-size:22px;color:#aaa}
.author{position:absolute;left:24px;top:232px;display:flex;align-items:center;gap:14px}
.avatar{width:80px;height:80px;border-radius:50%;background:linear-gradient(#dfe4ea,#9aa7b6);border:3px solid var(--white)}
.author-name{font-size:15px;font-style:italic;color:#222;border-bottom:1px solid var(--line);padding-bottom:10px;width:180px}
.author-name b{font-weight:500}
.mini-arrows{display:flex;gap:4px;margin-top:10px}
.mini-arrows span{width:20px;height:20px;border:1px solid #ccc;background:var(--white);display:flex;align-items:center;justify-content:center}

/* footer */
.site-footer{left:0;top:1988px;width:1200px;height:244px;background:var(--footer)}
.footer-col{top:31px}
.footer-col h6{font-size:15px;font-weight:400;color:var(--footer-text);letter-spacing:.3px}
.field{width:261px;height:42px;background:var(--footer-field);border:1px solid #262626;margin-top:14px;font-size:11px;color:#666;text-align:center;line-height:42px}
.field+.field{margin-top:8px}
.signup{display:block;width:261px;height:37px;line-height:37px;text-align:center;background:var(--blue);color:var(--white);font-size:13px;border-radius:3px;margin-top:14px}
.contact-lines{font-size:12.5px;line-height:21px;color:var(--footer-text);margin-top:14px;letter-spacing:.4px}
.contact-row{display:flex;align-items:center;gap:14px;margin-top:10px;font-size:13px;color:var(--footer-text)}
.info-list{list-style:none;margin-top:14px;border-right:1px solid #2c2c2c;padding-right:40px}
.info-list li{font-size:11px;color:var(--footer-text);line-height:20.7px}
.social-list{list-style:none;margin-top:14px}
.social-list li{font-size:12.5px;color:var(--footer-text);line-height:28px;display:flex;align-items:center;gap:13px}
.social-list li span{width:9px;height:9px;border-radius:50%;background:#9a9a9a}
.copyright{left:0;top:2232px;width:1200px;height:61px;background:var(--blue);color:var(--white);font-size:12px;text-align:center;line-height:61px}
</style>
</head>
<body>

<header class="site-header abs">
  <div class="header-contact abs" style="left:99px">
    <div class="icon-ring"><svg width="18" height="18" viewBox="0 0 24 24" fill="none" stroke="#444" stroke-width="1.8"><path d="M5 3h4l2 5-3 2a11 11 0 0 0 6 6l2-3 5 2v4a2 2 0 0 1-2 2A17 17 0 0 1 3 5a2 2 0 0 1 2-2z"/></svg></div>
    <div><div class="label">Call Us Now!</div><div class="value">+1 555.010.0148</div></div>
  </div>
  <div class="brand abs"><span class="brand-dot"></span><span class="brand-name">Corvanel</span></div>
  <div class="header-contact email abs" style="left:927px">
    <div class="icon-ring"><svg width="18" height="16" viewBox="0 0 24 20" fill="none" stroke="#444" stroke-width="1.8"><rect x="2" y="3" width="20" height="14" rx="1"/><path d="M2 4l10 7 10-7"/></svg></div>
    <div><div class="label">E - Mail</div><div class="value">info@corvanel-example.com</div></div>
  </div>
</header>

<nav class="main-nav abs">
  <ul>
    <li>HOME</li><li>ABOUT US</li><li>NEWS</li><li>OUR SERVICES</li><li>CONTACT US</li>
  </ul>
  <div class="nav-social abs"><span></span><span></span><span></span><span></span><span></span></div>
</nav>

<section class="hero abs" role="img" aria-label="Business team in a boardroom watching a presenter in front of a world route map">
  <h1 class="hero-title abs">Aviation Business Development</h1>
  <span class="hero-arrow abs" style="left:33px"><svg width="12" height="14" viewBox="0 0 12 14" fill="none" stroke="#fff" stroke-width="2"><path d="M8 2 3 7l5 5"/></svg></span>
  <span class="hero-arrow abs" style="left:1130px"><svg width="12" height="14" viewBox="0 0 12 14" fill="none" stroke="#fff" stroke-width="2"><path d="M4 2l5 5-5 5"/></svg></span>
</section>

<h2 class="section-title abs">OUR SERVICES</h2>
<span class="round-arrow abs" style="left:98px"><svg width="8" height="10" viewBox="0 0 8 10" fill="none" stroke="#333" stroke-width="1.5"><path d="M6 1 2 5l4 4"/></svg></span>
<span class="round-arrow abs" style="left:1074px"><svg width="8" height="10" viewBox="0 0 8 10" fill="none" stroke="#333" stroke-width="1.5"><path d="M2 1l4 4-4 4"/></svg></span>

<article class="service abs" style="left:98px">
  <div class="photo" role="img" aria-label="Engineer in a hard hat with colleagues reviewing plans" style="background:linear-gradient(135deg,#d9b98c,#7d8da0 60%,#e9e5df)"></div>
  <h3>Aviation Engineering</h3>
  <p>Lorem ipsum dolor sit amet, consectetur adipisicing elit, sed do eiusmod tempor incid-idunt ut labore et dolore magna</p>
  <a class="read-more">Read More</a>
</article>
<article class="service abs" style="left:354px">
  <div class="photo" role="img" aria-label="Consultants meeting around a table" style="background:linear-gradient(135deg,#e8e8e8,#8c8f98 50%,#cfd3da)"></div>
  <h3>Aviation consulting</h3>
  <p>Lorem ipsum dolor sit amet, consectetur adipisicing elit, sed do eiusmod tempor incid-idunt ut labore et dolore magna</p>
  <a class="read-more">Read More</a>
</article>
<article class="service abs" style="left:610px">
  <div class="photo" role="img" aria-label="Large yellow dump truck" style="background:linear-gradient(160deg,#c9d3dc,#e0b21c 50%,#6b6554)"></div>
  <h3>Aviation Equipment Supplies</h3>
  <p>Lorem ipsum dolor sit amet, consectetur adipisicing elit, sed do eiusmod tempor incid-idunt ut labore et dolore magna</p>
  <a class="read-more">Read More</a>
</article>
<article class="service abs" style="left:866px">
  <div class="photo" role="img" aria-label="Construction workers studying plans by a crane" style="background:linear-gradient(160deg,#9cc2e8,#c8d65a 55%,#6a8bb5)"></div>
  <h3>Aviation Construction Projects</h3>
  <p>Lorem ipsum dolor sit amet, consectetur adipisicing elit, sed do eiusmod tempor incid-idunt ut labore et dolore magna</p>
  <a class="read-more">Read More</a>
</article>

<section class="welcome abs">
  <div class="video abs">
    <div class="frame" role="img" aria-label="Passenger jet flying above a coastline"></div>
    <div class="bar">
      <svg width="8" height="9" viewBox="0 0 8 9"><path d="M0 0l8 4.5L0 9z" fill="#222"/></svg>
      <span>10:00/05:03</span>
      <span class="track"><i></i></span>
      <svg width="12" height="10" viewBox="0 0 12 10"><path d="M0 3h3l4-3v10L3 7H0z" fill="#222"/></svg>
      <span class="vol"></span>
    </div>
  </div>
  <div class="welcome-body abs">
    <h2>WELCOME TO <span>CORVANEL</span></h2>
    <p>Sed ut perspiciatis unde omnis istes err sit voluptatem accusantium doloremque laudantium, totam rem aperiam, eaque ipsa uae ab illo inventore veritatis et quasi architecto beatae vitae dicta sunt explicabo. Nemo enim ipsam voluptatem quia voluptas sit aspernatur aut odit aut fugit, sed quia conntur magni dolores eos qui ratione voluptatem sequi nesciunt.</p>
    <ul class="ticks">
      <li><span class="tick"></span>SED UT PERSPICIATIS UNDE OMNIS ISTE</li>
      <li><span class="tick"></span>ACCUSANTIUM DOLOREMQUE LAUDANT</li>
      <li><span class="tick"></span>ROTAM REM APERIAM EAQUE IPSA UAE</li>
    </ul>
    <a class="btn">CLICK HERE</a>
  </div>
</section>

<h3 class="col-title abs" style="left:98px;top:1560px">LATEST NEWS</h3>
<h3 class="col-title abs" style="left:807px;top:1560px">TESTIMONIALS</h3>

<article class="news-item abs" style="top:1608px">
  <div class="photo" role="img" aria-label="Business team gathered around a meeting table" style="background:linear-gradient(135deg,#f2f2f2,#7a7c82 55%,#d8d8d8)"></div>
  <div class="body">
    <h4>Nulla at diam ornare, aliquam urna vel,</h4>
    <div class="date">26 - FEB - 2015</div>
    <p>Nulla at diam ornare, aliquam urna vel, commodo urna. Nam id risus a est luctus consectetur quis eget libero. Suspendisse potenti. Pellentesque habitant morbi tristique senectus et netus et malesuada fames</p>
    <div class="more">READ MORE <svg width="11" height="11" viewBox="0 0 12 12"><circle cx="6" cy="6" r="6" fill="#1f56a8"/><path d="M5 3.5 7.5 6 5 8.5" stroke="#fff" stroke-width="1.5" fill="none"/></svg></div>
  </div>
</article>
<article class="news-item abs" style="top:1797px">
  <div class="photo" role="img" aria-label="Worker holding a hard hat near a building crane" style="background:linear-gradient(160deg,#6f9bd1,#c9a36a 55%,#7c6a55)"></div>
  <div class="body">
    <h4>Nulla at diam ornare, aliquam urna vel,</h4>
    <div class="date">26 - FEB - 2015</div>
    <p>Nulla at diam ornare, aliquam urna vel, commodo urna. Nam id risus a est luctus consectetur quis eget libero. Suspendisse potenti. Pellentesque habitant morbi tristique senectus et netus et malesuada fames</p>
    <div class="more">READ MORE <svg width="11" height="11" viewBox="0 0 12 12"><circle cx="6" cy="6" r="6" fill="#1f56a8"/><path d="M5 3.5 7.5 6 5 8.5" stroke="#fff" stroke-width="1.5" fill="none"/></svg></div>
  </div>
</article>

<aside class="testimonial abs">
  <h5>SED UT PERSPICIATIS UNDE OMNIS ISTE NATUS ERROR SIT VOLUP</h5>
  <p class="quote">Lorem ipsum dolor sit amet, consectetur adipisicing elit, sed do eiusmod tempor incididunt ut labore et dolore magna aliqua. Ut enim ad minim veniam, quis nostrud exercitation Lorem ipsum</p>
  <div class="author">
    <div class="avatar" role="img" aria-label="Client portrait"></div>
    <div>
      <div class="author-name"><b>John Doe</b> - agency</div>
      <div class="mini-arrows">
        <span><svg width="6" height="8" viewBox="0 0 6 8" fill="none" stroke="#333" stroke-width="1.4"><path d="M5 1 2 4l3 3"/></svg></span>
        <span><svg width="6" height="8" viewBox="0 0 6 8" fill="none" stroke="#333" stroke-width="1.4"><path d="M1 1l3 3-3 3"/></svg></span>
      </div>
    </div>
  </div>
</aside>

<footer class="site-footer abs">
  <div class="footer-col abs" style="left:120px">
    <h6>SIGN UP FOR NEWSLETTER</h6>
    <div class="field">Enter Name</div>
    <div class="field">Email</div>
    <a class="signup">SIGN UP NOW</a>
  </div>
  <div class="footer-col abs" style="left:485px">
    <h6>CONTACT US</h6>
    <div class="contact-lines">P.O. Box 210, Corvanel,<br>NC 00000</div>
    <div class="contact-row" style="margin-top:14px"><svg width="16" height="16" viewBox="0 0 24 24" fill="none" stroke="#9a9a9a" stroke-width="1.8"><path d="M5 3h4l2 5-3 2a11 11 0 0 0 6 6l2-3 5 2v4a2 2 0 0 1-2 2A17 17 0 0 1 3 5a2 2 0 0 1 2-2z"/></svg>+1 555 010 245 14</div>
    <div class="contact-row"><svg width="16" height="14" viewBox="0 0 24 20" fill="none" stroke="#9a9a9a" stroke-width="1.8"><rect x="2" y="3" width="20" height="14" rx="1"/><path d="M2 4l10 7 10-7"/></svg>info@corvanel-example.com</div>
  </div>
  <div class="footer-col abs" style="left:789px">
    <h6>INFORMATION</h6>
    <ul class="info-list">
      <li>HOME</li><li>ABOUT US</li><li>OUR SERVICES</li><li>NEWS &amp; INSIGHTS</li><li>CONTACT US</li><li>LOGIN</li>
    </ul>
  </div>
  <div class="footer-col abs" style="left:981px">
    <h6>SOCIAL</h6>
    <ul class="social-list">
      <li><span></span>Socialbook</li><li><span></span>Chirper</li><li><span></span>Circle Plus</li><li><span></span>ViewTube</li>
    </ul>
  </div>
</footer>

<div class="copyright abs">©2014 - 2015 &nbsp;Corvanel All Rights Reserved.</div>

</body>
</html>
```